New company website for Redfern Hollow Building Company

We're looking to build a new company website that customers can use to contact us, get quotes, view past projects (renovations, additions, new construction, etc.), & learn more about our business. We want to use WordPress for our website and have already purchased the Divi theme (by Quillmark Studio). Using that theme isn't required but we already have several examples of websites that we want to model our site after that use this theme. The "look" we're after is simple, light, & clean.

Target Market(s)

Residential remodeling, renovations, and new construction.

Industry/Entity Type

Residential Construction

Coding

Coded - Design and coding required

Number of Pages Required

5+ page

Font styles to use
Sans Serif

Colors
33a6d7
aaaaaa

Requirements
Must have
• We require the website to be coded using the Divi theme. We'll be upgrading the project to include this today or tomorrow.
• The navigation bar should be static & remain at the top of the page. When scrolling we'd like the logo & info in the nav bar to size down. Here's an example of a site that does this: https://tovamerihomes.example/
Nice to have
• In the gallery with pictures of our finished product/jobs, when you mouse over the image, we'd like there to be additional info that shows up. For example, look at this gallery: https://tovamerihomes.example/projectcategories/kitchens/ We'll add a name/location of the job like: "Garvey kitchen - Apex, N.C."
• If you go to this website: https://plinvorworks.example/ and scroll down to the pictures, we like how the picture moves and is interactive.

```html
<!DOCTYPE html>
<html lang="en">
<head>
<meta charset="utf-8">
<title>Redfern Hollow Building Company</title>
<link href="https://fonts.googleapis.com/css2?family=Montserrat:wght@400;500;600;700&display=swap" rel="stylesheet">
<style>
:root{
  --brand:#33a6d7;
  --button:#2e8fd6;
  --grey:#aaaaaa;
  --text:#666666;
  --dark:#333333;
  --light-bg:#f5f5f5;
  --card:#f7f7f7;
  --white:#ffffff;
  --footer-bar:#2e8fd6;
}
*{box-sizing:border-box;margin:0;padding:0}
html,body{width:1200px;height:3455px;overflow:hidden;background:var(--white)}
body{font-family:'Montserrat',sans-serif;color:var(--text);position:relative}
.page{position:relative;width:1200px;height:3455px;overflow:hidden}
.abs{position:absolute}

/* header */
.site-header{left:0;top:0;width:1200px;height:104px;background:var(--white);box-shadow:0 2px 6px rgba(0,0,0,.08);z-index:2}
.top-info{right:110px;top:20px;font-size:12px;color:var(--text);display:flex;gap:22px}
.top-info span{display:flex;align-items:center;gap:6px}
.brand-name{left:110px;top:58px;font-size:15px;font-weight:700;letter-spacing:2px;color:#555;text-transform:uppercase;line-height:17px}
.main-nav{right:110px;top:64px;display:flex;gap:28px;font-size:13.5px;font-weight:500;color:var(--dark);align-items:center}
.main-nav .active{color:var(--brand)}
.main-nav .drop::after{content:"";display:inline-block;width:5px;height:5px;border-right:1.5px solid #666;border-bottom:1.5px solid #666;transform:rotate(45deg);margin-left:8px;position:relative;top:-3px}

/* hero */
.hero{left:0;top:104px;width:1200px;height:463px;background:linear-gradient(180deg,#6f6a62 0%,#8b857b 40%,#5f5a52 100%)}
.hero-shade{left:0;top:104px;width:1200px;height:463px;background:rgba(0,0,0,.28)}
.hero-title{left:0;top:258px;width:1200px;text-align:center;font-size:38px;font-weight:500;color:var(--white)}
.btn{display:flex;align-items:center;justify-content:center;font-size:15px;font-weight:500;color:var(--white)}
.btn-ghost{left:392px;top:371px;width:173px;height:44px;border:2px solid var(--white);background:rgba(0,0,0,.15)}
.btn-solid{left:620px;top:371px;width:184px;height:44px;background:var(--button)}

/* features */
.feature{width:310px;text-align:center}
.feature h3{font-size:19px;font-weight:600;color:var(--brand);margin:52px 0 14px}
.feature p{font-size:13.5px;line-height:24px;color:#777}
.feature svg{position:absolute;left:130px;top:0}

/* gallery band */
.gallery-tile{top:806px;width:400px;height:269px;display:flex;align-items:center;justify-content:center}
.gallery-tile span{font-size:21px;color:var(--white);font-weight:400;position:relative}

/* transformations */
.section-title{font-size:25px;font-weight:600;color:var(--brand)}
.section-sub{font-size:16px;font-weight:600;color:#555}
.text-card{left:106px;top:1243px;width:458px;height:259px;background:var(--light-bg);padding:40px 28px}
.text-card p{font-size:13.5px;line-height:26px;color:#666}
.btn-blue{background:var(--button);color:var(--white);font-size:15px;font-weight:500;display:flex;align-items:center;justify-content:center}

/* specialities */
.spec-section{left:0;top:1573px;width:1200px;height:730px;background:var(--light-bg)}
.spec-text p{font-size:13.5px;line-height:24px;color:#666;margin-bottom:14px}
.photo{overflow:hidden}
.photo-card{position:absolute;background:rgba(255,255,255,.78);padding:28px 26px}
.photo-card h4{font-size:14.5px;font-weight:600;color:var(--brand);margin-bottom:18px}
.photo-card p{font-size:12.5px;line-height:24px;color:#777}

/* testimonials */
.testi-title{left:0;top:2372px;width:1200px;text-align:center;font-size:25px;font-weight:600;color:var(--dark)}
.testi-title em{font-style:normal;color:var(--brand)}
.avatar{width:82px;height:82px;border-radius:50%;top:2471px}
.testi-card{top:2591px;height:223px;background:var(--white);border:1px solid #ececec;box-shadow:0 1px 4px rgba(0,0,0,.05);text-align:center;padding:20px 24px}
.testi-card .quote{font-size:26px;color:var(--brand);font-weight:700;line-height:26px;height:28px}
.testi-card h5{font-size:15px;font-weight:600;color:var(--brand);margin:8px 0 14px}
.testi-card p{font-size:13.5px;line-height:24px;color:#555}
.dots{left:0;top:2854px;width:1200px;display:flex;justify-content:center;gap:8px}
.dots i{width:6px;height:6px;border-radius:50%;background:#ccc;display:block}
.dots i.on{background:#555}

/* footer */
.site-footer{left:0;top:2890px;width:1200px;height:514px;background:var(--light-bg)}
.footer-brand{left:106px;top:2952px;font-size:34px;font-weight:700;letter-spacing:4px;color:#555;line-height:40px;text-transform:uppercase}
.footer-intro{left:106px;top:3028px;width:400px;font-size:12.5px;line-height:22px;color:#666}
.footer-head{font-size:15px;font-weight:600;color:var(--brand)}
.footer-col ul{list-style:none;margin-top:10px}
.footer-col li{font-size:12.5px;line-height:25px;color:#666;position:relative;padding-left:14px}
.footer-col li::before{content:"";position:absolute;left:0;top:11px;width:4px;height:4px;border-radius:50%;background:var(--brand)}
.footer-contact{font-size:12.5px;line-height:22px;color:#666}
.footer-bar{left:0;top:3404px;width:1200px;height:51px;background:var(--footer-bar)}
.footer-bar .copy{position:absolute;left:106px;top:17px;font-size:12.5px;color:var(--white);font-weight:500}
.social{position:absolute;top:20px;width:12px;height:12px;border-radius:50%;background:var(--white)}
</style>
</head>
<body>
<div class="page">

  <!-- header -->
  <header class="site-header abs">
    <div class="top-info abs">
      <span><svg width="12" height="12" viewBox="0 0 24 24"><path d="M6.6 10.8c1.4 2.8 3.8 5.1 6.6 6.6l2.2-2.2c.3-.3.7-.4 1-.2 1.1.4 2.3.6 3.6.6.6 0 1 .4 1 1V20c0 .6-.4 1-1 1C10.6 21 3 13.4 3 4c0-.6.4-1 1-1h3.5c.6 0 1 .4 1 1 0 1.3.2 2.5.6 3.6.1.3 0 .7-.2 1z" fill="#666"/></svg>+919.555.0142</span>
      <span><svg width="13" height="10" viewBox="0 0 26 20"><rect x="1" y="1" width="24" height="18" fill="#666"/><path d="M1 1l12 10L25 1" stroke="#fff" stroke-width="2" fill="none"/></svg>info@redfernhollowbuilding.example</span>
    </div>
    <div class="brand-name abs">Redfern Hollow<br>Building Company</div>
    <nav class="main-nav abs">
      <span class="active">Home</span>
      <span class="drop">Getting Started</span>
      <span class="drop">Who We Are</span>
      <span class="drop">Specialities</span>
      <span class="drop">Portfolio</span>
      <span>Contact Us</span>
      <svg width="14" height="14" viewBox="0 0 24 24"><circle cx="10" cy="10" r="7" stroke="#666" stroke-width="2.5" fill="none"/><path d="M15 15l7 7" stroke="#666" stroke-width="2.5"/></svg>
    </nav>
  </header>

  <!-- hero -->
  <div class="hero abs" role="img" aria-label="Photo of a bright remodeled kitchen and dining area with pendant lights and a stone fireplace"></div>
  <div class="hero-shade abs"></div>
  <h1 class="hero-title abs">Your design and remodel partner for life</h1>
  <div class="btn btn-ghost abs">Our Specialties</div>
  <div class="btn btn-solid abs">Get a free Quote</div>

  <!-- features -->
  <div class="feature abs" style="left:96px;top:590px">
    <svg width="50" height="48" viewBox="0 0 50 48"><circle cx="25" cy="17" r="13" fill="#8a8a8a"/><circle cx="25" cy="17" r="7" fill="none" stroke="#fff" stroke-width="2"/><path d="M15 26l-5 16 7-3 4 6 4-12z M35 26l5 16-7-3-4 6-4-12z" fill="#8a8a8a"/></svg>
    <h3>Proven Trust</h3>
    <p>Home projects can be challenging. You need a company whose experience can lead to the result you want.</p>
  </div>
  <div class="feature abs" style="left:451px;top:590px">
    <svg width="52" height="48" viewBox="0 0 52 48"><rect x="2" y="8" width="34" height="22" rx="4" fill="#8a8a8a"/><path d="M10 30l-2 8 9-8z" fill="#8a8a8a"/><rect x="16" y="18" width="34" height="20" rx="4" fill="#fff" stroke="#8a8a8a" stroke-width="3"/><path d="M40 38l4 7-10-7z" fill="#8a8a8a"/></svg>
    <h3>Constant communication</h3>
    <p>Stay informed during every step of your project with your own SiteLedger account page.</p>
  </div>
  <div class="feature abs" style="left:780px;top:590px">
    <svg width="56" height="48" viewBox="0 0 56 48"><path d="M2 16l12-6 10 4 8-3 10 2 12 6-4 12-10 8-8 2-10-6-10-4z" fill="#8a8a8a"/><path d="M22 22l8 6M26 18l10 8M18 26l8 6" stroke="#fff" stroke-width="2"/></svg>
    <h3>History of Experience</h3>
    <p>We're focused on your goals and promise to always do what's best for you every step of the way.</p>
  </div>

  <!-- gallery band -->
  <div class="gallery-tile abs" style="left:0;background:linear-gradient(135deg,#5a5650,#7d766c 55%,#4b4741)" role="img" aria-label="Kitchens gallery photo of a finished kitchen"><span>Kitchens Gallery</span></div>
  <div class="gallery-tile abs" style="left:400px;background:linear-gradient(135deg,#4c4b4a,#6f6b66 55%,#3f3d3b)" role="img" aria-label="Bathrooms gallery photo of a finished bathroom"><span>Bathrooms Gallery</span></div>
  <div class="gallery-tile abs" style="left:800px;background:linear-gradient(180deg,#3d4456,#4d5568 60%,#5b5a50)" role="img" aria-label="Whole house gallery photo of a finished blue two-storey house"><span>Whole house Gallery</span></div>

  <!-- transformations -->
  <h2 class="section-title abs" style="left:106px;top:1150px">Transformations</h2>
  <div class="section-sub abs" style="left:106px;top:1190px">within your reach</div>
  <div class="text-card abs">
    <p>Lorem ipsum dolor sit amet, consectetur adipiscing elit, sed do eiusmod tempor incididunt ut labore et dolore magna aliqua. Ut enim ad minim veniam, quis nostrud exercitation ullamco laboris nisi ut aliquip ex ea commodo consequat.</p>
  </div>
  <div class="btn-blue abs" style="left:135px;top:1428px;width:247px;height:44px">View All Transformations</div>
  <div class="photo abs" style="left:619px;top:1152px;width:459px;height:281px;background:linear-gradient(180deg,#6f8a55 0%,#3f4d63 35%,#3a4560 65%,#b8a68a 85%,#a89478 100%)" role="img" aria-label="Photo of a new blue two-storey house with a front porch and garage"></div>

  <!-- specialities -->
  <div class="spec-section abs"></div>
  <h2 class="section-title abs" style="left:106px;top:1645px">Our Specialities</h2>
  <div class="spec-text abs" style="left:106px;top:1693px;width:460px">
    <p>Beautiful homes require brilliant thinking. Check out our latest insights, all inspired by client successes.</p>
    <p>Nobody provides quality like Redfern Hollow. Whether the project is interior or exterior, addition or kitchen, half-bath or bedroom, we have the know-how to make it happen.</p>
  </div>
  <div class="btn-blue abs" style="left:108px;top:1858px;width:196px;height:44px">View Our Portfolio</div>

  <div class="photo abs" style="left:619px;top:1644px;width:459px;height:293px;background:linear-gradient(135deg,#9a948a,#6f6a60 45%,#5a5448 70%,#8c7a60)" role="img" aria-label="Photo of a house addition among bare winter trees">
    <div class="photo-card" style="left:139px;top:99px;width:320px;height:194px">
      <h4>Addition</h4>
      <p>We're focused on your goals and promise to always do what's best for you every step of the way.</p>
    </div>
  </div>
  <div class="photo abs" style="left:106px;top:1962px;width:460px;height:290px;background:linear-gradient(180deg,#f3f2ee 0%,#e6e3dc 45%,#3f5a7d 70%,#6b5c4b 100%)" role="img" aria-label="Photo of a new kitchen with pendant lights and blue cabinets">
    <div class="photo-card" style="left:0;top:88px;width:320px;height:202px">
      <h4>New home construction</h4>
      <p>We're focused on your goals and promise to always do what's best for you every step of the way.</p>
    </div>
  </div>
  <div class="photo abs" style="left:619px;top:1962px;width:459px;height:290px;background:linear-gradient(180deg,#d9d9d6 0%,#bcbcb8 50%,#6d6760 85%,#5a544d 100%)" role="img" aria-label="Photo of a remodeled open living area with a staircase and ceiling fan">
    <div class="photo-card" style="left:139px;top:88px;width:320px;height:202px">
      <h4>Remodeling</h4>
      <p>We're focused on your goals and promise to always do what's best for you every step of the way.</p>
    </div>
  </div>

  <!-- testimonials -->
  <h2 class="testi-title abs"><em>Client</em> Testimonials</h2>
  <div class="avatar abs" style="left:210px;background:radial-gradient(circle,#b98f78,#7a5144)" role="img" aria-label="Client portrait"></div>
  <div class="avatar abs" style="left:550px;background:radial-gradient(circle,#b98f78,#7a5144)" role="img" aria-label="Client portrait"></div>
  <div class="avatar abs" style="left:893px;background:radial-gradient(circle,#b98f78,#7a5144)" role="img" aria-label="Client portrait"></div>

  <div class="testi-card abs" style="left:106px;width:290px">
    <div class="quote">&rdquo;</div>
    <h5>Clients Name</h5>
    <p>Lorem ipsum dolor sit amet, consectetur adipiscing elit, sed do eiusmod tempor incididunt ut labore et dolore magna aliqua.</p>
  </div>
  <div class="testi-card abs" style="left:449px;width:283px">
    <div class="quote">&rdquo;</div>
    <h5>Clients Name</h5>
    <p>Lorem ipsum dolor sit amet, consectetur adipiscing elit, sed do eiusmod tempor incididunt ut labore et dolore magna aliqua.</p>
  </div>
  <div class="testi-card abs" style="left:790px;width:288px;text-align:left">
    <div class="quote">&rdquo;</div>
    <h5>Client's name</h5>
    <p>Lorem ipsum dolor sit amet, consectetur adipiscing elit, sed do eiusmod tempor incididunt ut labore et dolore magna aliqua.</p>
  </div>
  <div class="dots abs"><i></i><i></i><i class="on"></i></div>

  <!-- footer -->
  <footer class="site-footer abs"></footer>
  <div class="footer-brand abs" style="font-size:22px;line-height:26px;letter-spacing:3px">Redfern Hollow<br>Building Company</div>
  <p class="footer-intro abs">Interested in a design-build project? Fill out our form below and we'll be in touch within 24 hours. Thank you for your interest in Redfern Hollow Building Company.</p>

  <div class="footer-head abs" style="left:106px;top:3143px">Contact Us</div>
  <div class="footer-contact abs" style="left:106px;top:3170px">Redfern Hollow Building Company<br>418 Cedar Mill Road, Suite 210<br>Larkton, TX 75990</div>
  <div class="footer-contact abs" style="left:106px;top:3254px;display:flex;align-items:center;gap:6px"><svg width="11" height="11" viewBox="0 0 24 24"><path d="M6.6 10.8c1.4 2.8 3.8 5.1 6.6 6.6l2.2-2.2c.3-.3.7-.4 1-.2 1.1.4 2.3.6 3.6.6.6 0 1 .4 1 1V20c0 .6-.4 1-1 1C10.6 21 3 13.4 3 4c0-.6.4-1 1-1h3.5c.6 0 1 .4 1 1 0 1.3.2 2.5.6 3.6.1.3 0 .7-.2 1z" fill="#666"/></svg>+919.555.0142</div>
  <div class="footer-contact abs" style="left:106px;top:3303px;display:flex;align-items:center;gap:6px"><svg width="12" height="9" viewBox="0 0 26 20"><rect x="1" y="1" width="24" height="18" fill="#666"/><path d="M1 1l12 10L25 1" stroke="#fff" stroke-width="2" fill="none"/></svg>info@redfernhollowbuilding.example</div>

  <div class="footer-col abs" style="left:619px;top:2950px">
    <div class="footer-head">Getting Started</div>
    <ul><li>What to expect</li><li>Our process</li><li>FAQs</li></ul>
  </div>
  <div class="footer-col abs" style="left:619px;top:3080px">
    <div class="footer-head">Specialties</div>
    <ul><li>Remodeling</li><li>New home construction</li><li>Additions</li></ul>
  </div>
  <div class="footer-col abs" style="left:619px;top:3212px">
    <div class="footer-head">Contact Us</div>
    <ul><li>Get Quotes</li><li>SiteLedger</li></ul>
  </div>
  <div class="footer-col abs" style="left:875px;top:2950px">
    <div class="footer-head">Who We Are</div>
    <ul><li>Our story</li><li>Redfern Hollow team</li><li>Testimonials</li></ul>
  </div>
  <div class="footer-col abs" style="left:875px;top:3080px">
    <div class="footer-head">Portfolio</div>
    <ul><li>Before and after</li><li>Kitchens</li><li>Bathrooms</li><li>Whole house</li></ul>
  </div>
  <div class="footer-col abs" style="left:875px;top:3237px;width:220px">
    <div class="footer-head" style="line-height:22px">Know Our Privacy<br>Policy</div>
    <ul><li>Privacy Policy</li><li>Disclaimer</li></ul>
  </div>

  <div class="footer-bar abs">
    <span class="copy">Copyright © 2018 Redfern Hollow Building Company.</span>
    <span class="social" style="left:988px"></span>
    <span class="social" style="left:1022px"></span>
    <span class="social" style="left:1056px"></span>
  </div>
</div>
</body>
</html>
```